依頼詳細
総合パンフレットの表紙と結果パンフレットの表紙に記載していただきたいものは以下の4つの項目です。
・スローガン「風見晴(かざみばれ)の北理競」※風見晴にはかざみばれというふりがなを付けてください。
・開催日程:2020年8月7日(金)~23日(日)
・第72回北嶺理工学生連合競技大会
・代表主管校:瑞光大学

総合パンフレットの裏表紙と結果パンフレットの裏表紙には以下の2つを記載していただきたいです。
・〒745-0172 梢県花川市緑町41 瑞光大学学生会館二階 第72回北理競運営室
・第72回北嶺理工学生連合競技大会運営委員会

サイズ
B5
ページ数
4ページ
希望イメージ
シンプル 複雑
単色 カラフル
暗い 明るい
日常 高級
遊び心 厳粛
未来的 伝統的
女性的 男性的
希望する色
納品ファイル
• イラストレーター形式 (.ai)
補足説明
ページ数は4ページとしておりますが、デザインがそろっていれば何ページでも大丈夫です。

イラストはイラストレーター形式にて縦長使用でお願いします。
そのまま印刷会社に入稿するので、カラーモードはCMYKにて、塗り足し・アウトライン化もお願いします。

ご提案を選択後に当選者様に修正を依頼する可能性がございますのでご了承ください。

選択させていただいたデザインの著作権(財産権)等の扱いはGigbrix利用規約に従い、弊運営委員会に譲渡をお願いします。

スローガンの色使い、背景の青が爽やかで夏の大会にふさわしいと感じました。

たくさんのご応募本当にありがとうございました。どれも素敵な作品ばかりで選ぶのが難しかったです。ご協力ありがとうございました。

```html
<!DOCTYPE html>
<html lang="ja">
<head>
<meta charset="utf-8">
<title>風見晴の北理競 — 第72回北嶺理工学生連合競技大会</title>
<link rel="stylesheet" href="https://fonts.googleapis.com/css2?family=M+PLUS+Rounded+1c:wght@500;700;900&display=swap">
<style>
  :root {
    --sky-top: #79b3dc;
    --sky-low: #cfe4ef;
    --sand-light: #e4c9a0;
    --sand-mid: #d5b385;
    --sand-deep: #c49f70;
    --slogan-pink: #ea4a86;
    --slogan-edge: #ffffff;
    --ruby-orange: #f39a2a;
    --ruby-green: #5cb531;
    --ruby-pink: #e0509a;
    --info-white: #ffffff;
    --info-shadow: rgba(120, 80, 40, 0.45);
  }
  * { margin: 0; padding: 0; box-sizing: border-box; }
  html, body {
    width: 848px;
    height: 1200px;
    overflow: hidden;
    background: #ffffff;
  }
  .cover {
    position: relative;
    width: 848px;
    height: 1200px;
    overflow: hidden;
    font-family: "M PLUS Rounded 1c", sans-serif;
  }
  .cover-backdrop {
    position: absolute;
    inset: 0;
    background: linear-gradient(180deg,
      var(--sky-top) 0%,
      var(--sky-low) 19%,
      var(--sand-light) 23%,
      var(--sand-mid) 55%,
      var(--sand-deep) 100%);
  }
  .slogan {
    position: absolute;
    left: 0;
    top: 360px;
    width: 848px;
    height: 380px;
  }
  .slogan text {
    font-family: "M PLUS Rounded 1c", sans-serif;
    font-weight: 900;
    paint-order: stroke fill;
    stroke-linejoin: round;
  }
  .slogan-main {
    font-size: 200px;
    fill: var(--slogan-pink);
    stroke: var(--slogan-edge);
    stroke-width: 16px;
  }
  .slogan-sub {
    font-size: 88px;
    fill: var(--slogan-pink);
    stroke: var(--slogan-edge);
    stroke-width: 12px;
  }
  .slogan-ruby {
    font-size: 34px;
    stroke: var(--slogan-edge);
    stroke-width: 6px;
  }
  .ruby-orange { fill: var(--ruby-orange); }
  .ruby-green { fill: var(--ruby-green); }
  .ruby-pink { fill: var(--ruby-pink); }
  .event-info {
    position: absolute;
    left: 0;
    top: 985px;
    width: 848px;
    color: var(--info-white);
    text-shadow: 0 1px 4px var(--info-shadow);
    text-align: center;
  }
  .event-name {
    font-size: 32px;
    font-weight: 500;
    letter-spacing: 0.02em;
  }
  .event-dates {
    margin-top: 8px;
    font-size: 46px;
    font-weight: 500;
    letter-spacing: 0.01em;
  }
  .event-host {
    margin-top: 10px;
    padding-left: 160px;
    font-size: 22px;
    font-weight: 500;
  }
</style>
</head>
<body>
  <main class="cover">
    <div class="cover-backdrop" role="img" aria-label="夏空の下に広がる砂丘の風紋写真と、その上を舞う色とりどりの羽根のイラスト"></div>

    <svg class="slogan" viewBox="0 0 848 380" aria-label="風見晴(かざみばれ)の北理競">
      <text class="slogan-ruby ruby-orange" x="200" y="34" text-anchor="middle">かざ</text>
      <text class="slogan-ruby ruby-green" x="424" y="34" text-anchor="middle">み</text>
      <text class="slogan-ruby ruby-pink" x="634" y="34" text-anchor="middle">ばれ</text>
      <text class="slogan-main" x="424" y="225" text-anchor="middle" textLength="640" lengthAdjust="spacingAndGlyphs">風見晴</text>
      <text class="slogan-sub" x="424" y="348" text-anchor="middle">の北理競</text>
    </svg>

    <section class="event-info">
      <p class="event-name">第72回 北嶺理工学生連合競技大会</p>
      <p class="event-dates">2020年8月7日(金)~23日(日)</p>
      <p class="event-host">代表主管校:瑞光大学</p>
    </section>
  </main>
</body>
</html>
```